Corvalent Ventures Sales Materials & Look

I am looking for an impactful design to a sales/presentation folder.

On the top of the folder I want the power quotes
Pure Nutrition From Phytoplankton
The World's Original Whole Food
The Best Results In Natural Health History

*picture of powder
Corvalent logo.

The colors and font on the corvalent logo are important to keep in tact even for the power quotes.
I'll leave it up to you how you want to stylize it.

On the back on the bottom (subtle) I want the following
Logo
Unit #6 - 482 Larkspur Road
Moncton, New Brunswick
Canada
(506) 555 0147
Plus any other styling you want to consider.

We sell marine phytoplankton powder to other businesses. Marine Phytoplankton is the original vegetable on the planet. It's positioned as a natural medicine for chrohn's and colitis, and fibromyalgia.

I have added the business card design. Please add the following information
Martin Oakes - Founder - CEO
email - mjoakes@corvalent.example
Phone - (506) 555 0192
Corvalent Ventures Inc
Unit #6 - 482 Larkspur Road
Moncton, New Brunswick
E2K 4R7
Canada

```html
<!DOCTYPE html>
<html lang="en">
<head>
<meta charset="utf-8">
<title>Corvalent Ventures Inc — Business Card</title>
<link href="https://fonts.googleapis.com/css2?family=Raleway:wght@400;500;600;800&display=swap" rel="stylesheet">
<style>
  :root {
    --brand-blue: #29a6e0;
    --brand-blue-deep: #1f9ad6;
    --brand-green: #8dc63f;
    --ink: #4a4a4a;
    --rule: #b8b8b8;
    --paper: #ffffff;
    --backdrop: #e9eaec;
  }
  * { box-sizing: border-box; margin: 0; padding: 0; }
  html, body { width: 1200px; height: 1200px; overflow: hidden; }
  body {
    background: var(--backdrop);
    font-family: "Raleway", Arial, sans-serif;
    position: relative;
  }
  .card {
    position: absolute;
    left: 180px;
    width: 840px;
    height: 480px;
    border-radius: 40px;
    overflow: hidden;
    box-shadow: 0 14px 30px rgba(0,0,0,0.18);
  }
  .card--front { top: 90px; background: var(--paper); }
  .card--back {
    top: 630px;
    background: linear-gradient(120deg, var(--brand-blue-deep) 0%, #3db3e6 50%, var(--brand-blue-deep) 100%);
  }

  /* brand lockup */
  .brand {
    position: absolute;
    display: flex;
    align-items: center;
    gap: 18px;
  }
  .brand__dot {
    border-radius: 50%;
    flex: none;
  }
  .brand__name {
    font-weight: 800;
    line-height: 1;
    letter-spacing: -0.5px;
  }
  .card--front .brand { left: 190px; top: 110px; }
  .card--front .brand__dot { width: 46px; height: 46px; background: var(--brand-green); }
  .card--front .brand__name { font-size: 56px; color: var(--brand-blue); }

  .card--back .brand { left: 50%; top: 50%; transform: translate(-50%, -50%); }
  .card--back .brand__dot { width: 70px; height: 70px; background: #ffffff; }
  .card--back .brand__name { font-size: 78px; color: #ffffff; }

  /* person */
  .person {
    position: absolute;
    left: 150px;
    top: 330px;
  }
  .person__name {
    font-size: 30px;
    font-weight: 600;
    color: var(--brand-blue);
    letter-spacing: -0.5px;
    line-height: 1.1;
  }
  .person__role {
    font-size: 24px;
    font-weight: 500;
    color: var(--ink);
    line-height: 1.2;
  }

  .divider {
    position: absolute;
    left: 440px;
    top: 250px;
    width: 1px;
    height: 90px;
    background: var(--rule);
  }

  /* contact */
  .contact {
    position: absolute;
    left: 470px;
    top: 225px;
    list-style: none;
    font-size: 17px;
    color: var(--ink);
    line-height: 1.35;
  }
  .contact__item {
    display: flex;
    align-items: flex-start;
    gap: 10px;
  }
  .contact__icon {
    width: 18px;
    height: 18px;
    flex: none;
    margin-top: 2px;
    fill: var(--brand-blue);
  }
  .contact__item--address .contact__icon { margin-top: 24px; }

  /* bottom bands */
  .band {
    position: absolute;
    bottom: 0;
  }
  .band--blue {
    left: 0;
    width: 525px;
    height: 22px;
    background: var(--brand-blue);
  }
  .band--green {
    right: 0;
    width: 305px;
    height: 44px;
    background: var(--brand-green);
  }
</style>
</head>
<body>

  <section class="card card--front" aria-label="Business card front">
    <div class="brand">
      <span class="brand__dot"></span>
      <span class="brand__name">Corvalent Ventures Inc</span>
    </div>

    <div class="person">
      <p class="person__name">MARTIN OAKES</p>
      <p class="person__role">Founder | CEO</p>
    </div>

    <div class="divider"></div>

    <ul class="contact">
      <li class="contact__item">
        <svg class="contact__icon" viewBox="0 0 24 24" aria-hidden="true"><path d="M6.6 10.8a15.1 15.1 0 0 0 6.6 6.6l2.2-2.2a1 1 0 0 1 1-.25 11.4 11.4 0 0 0 3.6.57 1 1 0 0 1 1 1V20a1 1 0 0 1-1 1A17 17 0 0 1 3 4a1 1 0 0 1 1-1h3.5a1 1 0 0 1 1 1c0 1.25.2 2.45.57 3.6a1 1 0 0 1-.25 1z"/></svg>
        <span>(506) 555 0192</span>
      </li>
      <li class="contact__item">
        <svg class="contact__icon" viewBox="0 0 24 24" aria-hidden="true"><path d="M2 5h20v14H2zm2 2v.5l8 5 8-5V7zm0 3v7h16v-7l-8 5z"/></svg>
        <span>mjoakes@corvalent.example</span>
      </li>
      <li class="contact__item contact__item--address">
        <svg class="contact__icon" viewBox="0 0 24 24" aria-hidden="true"><path d="M12 2a7 7 0 0 0-7 7c0 5.2 7 13 7 13s7-7.8 7-13a7 7 0 0 0-7-7zm0 9.5A2.5 2.5 0 1 1 12 6.5a2.5 2.5 0 0 1 0 5z"/></svg>
        <span>Corvalent Ventures Inc<br>Unit #6 - 482 Larkspur Road Moncton<br>New Brunswick E2K 4R7 Canadá</span>
      </li>
    </ul>

    <div class="band band--blue"></div>
    <div class="band band--green"></div>
  </section>

  <section class="card card--back" aria-label="Business card back">
    <div class="brand">
      <span class="brand__dot"></span>
      <span class="brand__name">Corvalent</span>
    </div>
  </section>

</body>
</html>
```